Baseball Trainer Poster

Looking to put up a poster inside an indoor baseball facility which markets the cost of instruction, but also the trainers who can be hired.
I have done a crude job of building a Power Point which includes the pictures and general details. I was hoping you could crop the pictures of the coaches as needed.
I have also attached our logo.
I have also attached a generic flier we had made for a camp previously.
Name of Indoor Facility is "Bolt Yard"
Just FYI: website is www.BoltYardGym.example
The ideal colors for the poster are Blue, Red, White & Grey

```html
<!DOCTYPE html>
<html lang="en">
<head>
<meta charset="utf-8">
<title>Bolt Yard – Personal Instruction Poster</title>
<link href="https://fonts.googleapis.com/css2?family=Barlow+Condensed:wght@700;800&family=Barlow:wght@500;700&family=Montserrat:ital,wght@0,500;0,700;0,800;1,800;1,900&display=swap" rel="stylesheet">
<style>
  :root{
    --bg:#7a7a7a;
    --navy:#0f2340;
    --navy-deep:#142a4a;
    --red:#e0301e;
    --red-bright:#ff3b1f;
    --grey:#c9cdd2;
    --white:#ffffff;
    --photo-a:#6d7a8a;
    --photo-b:#3c4a5c;
  }
  *{margin:0;padding:0;box-sizing:border-box}
  html,body{width:1200px;height:1000px;overflow:hidden;background:var(--bg)}
  .poster{position:absolute;left:303px;top:86px;width:592px;height:841px;background:var(--white);overflow:hidden;font-family:"Montserrat",sans-serif}
  .poster-bands{position:absolute;inset:0}
  .brand{position:absolute;left:48px;top:22px;width:164px;height:164px;border-radius:50%;background:var(--white);border:6px solid var(--navy);display:flex;align-items:center;justify-content:center}
  .brand-name{font-family:"Barlow Condensed",sans-serif;font-weight:800;font-size:40px;color:var(--navy)}
  .title{position:absolute;left:238px;top:22px;font-family:"Barlow Condensed",sans-serif;font-weight:800;font-size:32px;color:var(--navy);letter-spacing:.3px}
  .price{position:absolute;left:238px;width:317px;height:27px;background:var(--red);border-radius:4px;color:var(--white);font-family:"Barlow",sans-serif;font-weight:700;font-size:16px;display:flex;align-items:center;justify-content:center}
  .banner{position:absolute;height:30px;display:flex;align-items:center;justify-content:center;font-weight:900;font-style:italic;font-size:23px;color:var(--navy);letter-spacing:.5px}
  .banner::before{content:"";position:absolute;inset:0;background:var(--grey);transform:skewX(-25deg);z-index:0}
  .banner span{position:relative}
  .trainer{position:absolute;width:180px;text-align:center}
  .trainer-photo{display:block;margin:0 auto;width:137px;height:75px;border:3px solid var(--white);background:linear-gradient(160deg,var(--photo-a),var(--photo-b))}
  .trainer-name{margin-top:12px;color:var(--red-bright);font-weight:800;font-size:8.5px;line-height:1.3}
  .trainer-role{margin-top:4px;color:var(--white);font-weight:500;font-size:8.5px;line-height:1.45}
  .coach{position:absolute;width:136px;text-align:center}
  .coach-photo{display:block;margin:0 auto;width:60px;height:60px;border-radius:50%;border:3px solid var(--red);background:linear-gradient(160deg,#9aa3ad,#4a5462)}
  .coach-name{margin-top:11px;color:var(--red);font-weight:800;font-size:8px}
  .coach-role{margin-top:3px;color:#333;font-family:"Barlow",sans-serif;font-weight:500;font-size:7.4px;line-height:1.45}
  .divider{position:absolute;width:1px;background:#d6d6d6}
  .footer{position:absolute;left:0;bottom:0;width:100%;height:36px;background:var(--red);display:flex;align-items:center;justify-content:center;color:var(--white);font-weight:900;font-style:italic;font-size:16px}
</style>
</head>
<body>
<div class="poster">
  <svg class="poster-bands" width="592" height="841" viewBox="0 0 592 841" aria-hidden="true">
    <polygon points="0,145 592,150 592,248 0,240" fill="var(--red)"/>
    <polygon points="0,175 592,138 592,176 0,200" fill="var(--red-bright)"/>
    <polygon points="0,240 592,220 592,552 0,552" fill="var(--navy)"/>
    <polygon points="0,252 592,236 592,270 0,290" fill="var(--navy-deep)"/>
    <polygon points="0,538 592,532 592,585 0,576" fill="var(--red)"/>
    <polygon points="0,576 592,560 592,585 0,592" fill="var(--red-bright)"/>
    <polygon points="0,592 592,585 592,600 0,600" fill="var(--white)"/>
  </svg>

  <div class="brand"><span class="brand-name">Bolt Yard</span></div>
  <h1 class="title">PERSONAL INSTRUCTION</h1>
  <div class="price" style="top:60px">$35 for tandem lesson (2:1)/Half-HR</div>
  <div class="price" style="top:92px">$50 for private lesson/Half-HR</div>
  <div class="price" style="top:124px">$150 to train 4+ players/1-Hour</div>

  <div class="banner" style="left:122px;top:200px;width:350px"><span>PRIVATE INSTUCTION</span></div>

  <div class="trainer" style="left:12px;top:250px">
    <div class="trainer-photo" role="img" aria-label="Photo of Derek Alvaro"></div>
    <div class="trainer-name">DEREK ALVARO –</div>
    <div class="trainer-role">Former Pro Pitcher Minor League<br>(Harbor Hawks &amp; Mesa Suns)</div>
  </div>
  <div class="trainer" style="left:205px;top:250px">
    <div class="trainer-photo" role="img" aria-label="Photo of Colin Barrett"></div>
    <div class="trainer-name">COLIN BARRETT –</div>
    <div class="trainer-role">Former Pro Pitcher Minor League<br>(River Kings, Bay Herons, Lakeport)</div>
  </div>
  <div class="trainer" style="left:399px;top:250px">
    <div class="trainer-photo" role="img" aria-label="Photo of Mitch Halden with his team"></div>
    <div class="trainer-name">MITCH HALDEN; FORMER PRO<br>PITCHER (COASTLINERS) –</div>
    <div class="trainer-role">Pitching &amp; Hitting Instructor</div>
  </div>
  <div class="trainer" style="left:12px;top:392px">
    <div class="trainer-photo" role="img" aria-label="Photo of Reid Marano"></div>
    <div class="trainer-name">REID MARANO –</div>
    <div class="trainer-role">Hitting Played professionally after<br>College in the Independent League<br>on the West Coach</div>
  </div>
  <div class="trainer" style="left:205px;top:392px">
    <div class="trainer-photo" role="img" aria-label="Photo of Kyle Warden"></div>
    <div class="trainer-name">KYLE WARDEN –</div>
    <div class="trainer-role">Infield &amp; Hitting Current College<br>Coach; Former College Shortstop</div>
  </div>
  <div class="trainer" style="left:399px;top:392px">
    <div class="trainer-photo" role="img" aria-label="Photo of Grant Carlow"></div>
    <div class="trainer-name">GRANT CARLOW –</div>
    <div class="trainer-role">Catching &amp; Hitting Current<br>HS Coach &amp; 16u Showcase Coach</div>
  </div>

  <div class="banner" style="left:206px;top:540px;width:186px"><span>LESSONS</span></div>

  <div class="divider" style="left:158px;top:590px;height:210px"></div>
  <div class="divider" style="left:297px;top:590px;height:210px"></div>
  <div class="divider" style="left:436px;top:590px;height:210px"></div>

  <div class="coach" style="left:21px;top:584px">
    <div class="coach-photo" role="img" aria-label="Photo of Alex Dorsey"></div>
    <div class="coach-name">ALEX DORSEY –</div>
    <div class="coach-role">Hitting &amp; Pitching Former College<br>Coach &amp; Current High School</div>
  </div>
  <div class="coach" style="left:159px;top:584px">
    <div class="coach-photo" role="img" aria-label="Photo of Zane Norwood"></div>
    <div class="coach-name">ZANE NORWOOD–</div>
    <div class="coach-role">Hitting &amp; Defense Former College<br>Player &amp; former HS Coach</div>
  </div>
  <div class="coach" style="left:298px;top:584px">
    <div class="coach-photo" role="img" aria-label="Photo of Kurt Sallis"></div>
    <div class="coach-name">KURT SALLIS-</div>
    <div class="coach-role">Hitting &amp; Infield Former College &amp; former<br>Pro Player Current 16u Showcase Coach</div>
  </div>
  <div class="coach" style="left:436px;top:584px">
    <div class="coach-photo" role="img" aria-label="Photo of Jonah Galvez"></div>
    <div class="coach-name">JONAH GALVEZ –</div>
    <div class="coach-role">Catching &amp; Hitting Current college<br>coach; works Bolt Yard's Camps</div>
  </div>
  <div class="coach" style="left:21px;top:691px">
    <div class="coach-photo" role="img" aria-label="Photo of Ross Sutter"></div>
    <div class="coach-name">ROSS SUTTER–</div>
    <div class="coach-role">Catching &amp; Hitting Current College<br>Coach &amp; former player</div>
  </div>
  <div class="coach" style="left:159px;top:691px">
    <div class="coach-photo" role="img" aria-label="Photo of Pete Kessler"></div>
    <div class="coach-name">PETE KESSLER –</div>
    <div class="coach-role">Hitting &amp; Catching Former<br>College Coach &amp; HS Head Coach</div>
  </div>
  <div class="coach" style="left:298px;top:691px">
    <div class="coach-photo" role="img" aria-label="Photo of Matt Warden"></div>
    <div class="coach-name">MATT WARDEN –</div>
    <div class="coach-role">Hitting &amp; Defense Current HS Head<br>Coach and 15u Showcase Coach</div>
  </div>
  <div class="coach" style="left:436px;top:691px">
    <div class="coach-photo" role="img" aria-label="Photo of Gavin Sahota"></div>
    <div class="coach-name">GAVIN SAHOTA -</div>
    <div class="coach-role">Hitting &amp; Infield Former College<br>Player &amp; Current HS Coach</div>
  </div>

  <div class="footer">www.BoltYardGym.example</div>
</div>
</body>
</html>
```